Modellprojekt in der Jugendhilfe sucht für Abschlussbroschüre ansprechendes Design
Zielgruppe
Wir sind ein Jugendhilfeträger und haben kürzlich ein dreijähriges Modellprojekt 'Qualitätsmarke-Gemeinsame Familienbegleitung' (Signet 'QM_Anerkennung' liegt anbei) beendet. Zielgruppen sind zum Einen Kinder und Jugendliche, die in Erziehungshilfe-Wohngruppen leben und zum Anderen Fach- und Führungskräfte in der Kinder- und Jugendhilfe. Über Ablauf und Schlussfolgerungen aus dem abgeschlossenen Modellprojekt soll eine 30-seitige Broschüre mit dem Titel 'Hier wächst Mitsprache' Untertitel 'Ein Wegweiser zur Qualitätsmarke' Auskunft geben.
Aufgabenstellung
- Broschüre im DIN A4 - Format,
- Dummy-Text für Projektstruktur und -beteiligte,
- Formschönes und dynamisches Design,
- Platzhalter für eigene Bilder (max. 3 pro Seite),
- die 6 Einrichtungslogos in einer Reihe auf dem Deckblatt vorne (unten),
- Der Broschüreninhalt ist in der PDF 'Kurzvorstellung enthalten',
- Vorgaben zum CD im PDF 'Hauptmanual KWF',
- Das KWF-Signet, wie im Manual beschrieben,
- das ebenfalls hochgeladene Gütesiegel kommt auf das Deckblatt

```html
<!DOCTYPE html>
<html lang="de">
<head>
<meta charset="utf-8">
<title>Hier wächst Mitsprache – Impressum und Inhalt</title>
<link rel="stylesheet" href="https://fonts.googleapis.com/css2?family=Fira+Sans:wght@300;400;500;700&family=Noto+Serif:wght@700&display=swap">
<style>
  :root {
    --backdrop: #e2e2e2;
    --paper: #f4f4f4;
    --ink: #1e1e1e;
    --navy: #1a2654;
    --royal: #1a4290;
    --steel: #4a7fb8;
    --panel: #d3dcea;
    --heading-blue: #1f4a8c;
    --photo-warm: #d9c2a8;
    --photo-cool: #e7ebee;
  }
  * { box-sizing: border-box; margin: 0; padding: 0; }
  html, body { width: 1200px; height: 960px; overflow: hidden; }
  body {
    background: var(--backdrop);
    font-family: "Fira Sans", sans-serif;
    color: var(--ink);
    position: relative;
  }
  .spread {
    position: absolute;
    left: 60px; top: 100px;
    width: 1080px; height: 760px;
    display: flex;
  }
  .page {
    position: relative;
    width: 540px; height: 760px;
    background: var(--paper);
  }
  .page--left { border-right: 1px solid #dcdcdc; }

  /* Impressum page */
  .ornament-area {
    position: absolute;
    left: 60px; top: 220px;
    width: 200px; height: 210px;
    background: linear-gradient(135deg, var(--navy) 0%, var(--royal) 55%, var(--steel) 100%);
    opacity: 0.85;
  }
  .imprint {
    position: absolute;
    left: 150px; top: 450px;
    width: 280px;
  }
  .imprint__title {
    font-weight: 700;
    font-size: 24px;
    line-height: 1.2;
    margin-bottom: 10px;
  }
  .imprint__text {
    font-weight: 500;
    font-size: 11.5px;
    line-height: 1.38;
    margin-bottom: 14px;
  }

  /* Inhalt page */
  .contents-photo {
    position: absolute;
    left: 30px; top: 60px;
    width: 440px; height: 240px;
    background: linear-gradient(100deg, var(--photo-cool) 0%, var(--photo-warm) 45%, #c9a383 70%, var(--photo-cool) 100%);
  }
  .contents-panel {
    position: absolute;
    left: 80px; top: 220px;
    width: 440px; height: 400px;
    background: var(--panel);
    padding: 84px 34px 0 30px;
  }
  .contents-title {
    position: absolute;
    left: 96px; top: 236px;
    font-family: "Noto Serif", serif;
    font-weight: 700;
    font-size: 46px;
    line-height: 1.2;
    color: var(--heading-blue);
  }
  .toc { list-style: none; }
  .toc__item {
    display: flex;
    align-items: baseline;
    font-weight: 300;
    font-size: 12px;
    line-height: 1.2;
    color: #333;
    margin-bottom: 16px;
    white-space: nowrap;
  }
  .toc__leader {
    flex: 1;
    border-bottom: 1px dotted #555;
    margin: 0 4px;
    transform: translateY(-3px);
  }
</style>
</head>
<body>
  <main class="spread">
    <section class="page page--left">
      <div class="ornament-area" role="img" aria-label="Dekoratives Formenmotiv aus Halbkreis, Rechtecken und Oval in Blautönen"></div>
      <div class="imprint">
        <h2 class="imprint__title">Impressum</h2>
        <p class="imprint__text">Ignihilit, ullab id quias ipsamendebis ipsum velendi ssitatum que voloriatur, voloritia natati-is dolorec temodi quis nimusap erferi optatquam aceped molupti umquat entur? Il eumque debis molum ut quas esti aut am aspitet, que optatib eribus ipienti bearchic te voloriae dipsa si blaudan dipsam quodita errovi-ta voloritis sunt aspis veritia a eos alibus auda dem suntem eaquiae prorionse sae. Obitiore nos eturio iumquiatas doluptio volorum simus. Igendicte labo. Ut as quia dolorro vitenet re</p>
        <p class="imprint__text">Ignihilit, ullab id quias ipsamendebis ipsum velendi ssitatum que voloriatur, voloritia natati-is dolorec temodi quis nimusap erferi optatquam aceped molupti umquat entur?</p>
      </div>
    </section>

    <section class="page page--right">
      <div class="contents-photo" role="img" aria-label="Foto: lachende Jugendliche sitzen gemeinsam in einem hellen Raum"></div>
      <div class="contents-panel">
        <ol class="toc">
          <li class="toc__item"><span>Danksagung Th. Brenner</span><span class="toc__leader"></span><span>3</span></li>
          <li class="toc__item"><span>Erfolgsstory (Best Practise – Vorstellung vor Ort)</span><span class="toc__leader"></span><span>4</span></li>
          <li class="toc__item"><span>Hier wächst Mitsprache – eine partizipative Lernreise</span><span class="toc__leader"></span><span>6</span></li>
          <li class="toc__item"><span>Lernreiseteilnehmer</span><span class="toc__leader"></span><span>7</span></li>
          <li class="toc__item"><span>Ladestationen auf dem Weg zur Qualitätsmarke</span><span class="toc__leader"></span><span>8</span></li>
          <li class="toc__item"><span>Lernreise-Highlight Campus – Ein Erlebnis mit Ergebnis</span><span class="toc__leader"></span><span>15</span></li>
          <li class="toc__item"><span>Heimkehr / Finale mit Befragung</span><span class="toc__leader"></span><span>19</span></li>
          <li class="toc__item"><span>Zum Abschluss: Ihr Fahrplan zur „Qualitätsmarke“</span><span class="toc__leader"></span><span>22</span></li>
          <li class="toc__item"><span>Quellen</span><span class="toc__leader"></span><span>29</span></li>
        </ol>
      </div>
      <h1 class="contents-title">Inhalt</h1>
    </section>
  </main>
</body>
</html>
```